Social Media Cover and Profile

We already have our own logo. We just need a fresh design on our social media pages. We are not happy with our current designs. We would like to incorporate our YIKE billboard and the colors are blue (#05143f) and white. You can also incorporate silver as well. We are a family law office (Divorce and Custody) We no longer want to incorporate the Spire of Dunvale photo that we are currently using. You can look at our Friendbook page; The Law Office of Miles T. Hadley.

Target Market(s)

Potential Clients

Industry/Entity Type

Family Law

Logo Text

Our Logo Is The Law Office of Miles T. Hadley with the Sheild

Requirements
Must have
• Text to include:
Central Pennslyvania's Premier Family Law Firm

Ability to be resized to and used as all images in social media, including but not limited to: ViewTube Channel art, Friendbook Cover and Profile.
Nice to have
• Darker color but we are open to "bright" ideas.

```html
<!DOCTYPE html>
<html lang="en">
<head>
<meta charset="utf-8">
<title>Miles T. Hadley – Social Covers</title>
<link rel="stylesheet" href="https://fonts.googleapis.com/css2?family=EB+Garamond:wght@400;600&family=Montserrat:wght@400;600;700;800&family=Open+Sans:wght@400&display=swap">
<style>
  :root {
    --navy: #05143f;
    --white: #ffffff;
    --silver: #8b8d92;
    --silver-light: #d9dadd;
    --ink: #1c1f2a;
    --stage-top: #8a8a8a;
    --stage-bottom: #353535;
  }
  * { box-sizing: border-box; margin: 0; padding: 0; }
  html, body { width: 1200px; height: 960px; overflow: hidden; }
  body {
    position: relative;
    background: linear-gradient(160deg, var(--stage-top) 0%, #666 50%, var(--stage-bottom) 100%);
    font-family: "Montserrat", sans-serif;
  }
  .format-label {
    position: absolute;
    left: 0; width: 100%;
    text-align: center;
    font-family: "Open Sans", sans-serif;
    font-size: 27px;
    color: var(--white);
    letter-spacing: 0.5px;
  }
  .format-label--page { top: 86px; padding-left: 0; }
  .format-label--channel { top: 514px; padding-right: 14px; }

  .cover {
    position: absolute;
    background: var(--white);
    box-shadow: 0 18px 22px -14px rgba(0,0,0,0.55);
    overflow: hidden;
  }
  .cover--page { left: 240px; top: 158px; width: 719px; height: 273px; }
  .cover--channel { left: 69px; top: 586px; width: 1062px; height: 175px; }

  .tagline-panel {
    position: absolute; left: 0; top: 0; height: 100%;
    background: var(--navy);
    color: var(--white);
    font-family: "EB Garamond", serif;
  }
  .cover--page .tagline-panel { width: 283px; }
  .cover--channel .tagline-panel { width: 279px; }
  .tagline { position: absolute; font-weight: 400; }
  .tagline strong { font-weight: 600; }
  .tagline span { display: block; }
  .cover--page .tagline { left: 30px; top: 28px; font-size: 35px; line-height: 42px; }
  .cover--channel .tagline { left: 33px; top: 18px; font-size: 30px; line-height: 34.5px; }
  .tagline-rule {
    position: absolute; left: 30px; top: 211px;
    width: 136px; height: 1px; background: rgba(255,255,255,0.7);
  }

  .rings {
    position: absolute;
    background: radial-gradient(ellipse at center, #f4f4f5 0%, var(--silver-light) 60%, #eeeff1 100%);
    border-radius: 4px;
  }
  .cover--page .rings { left: 313px; top: 67px; width: 203px; height: 120px; }
  .cover--channel .rings { left: 312px; top: 18px; width: 209px; height: 122px; }

  .billboard-word {
    position: absolute;
    font-family: "Montserrat", sans-serif;
    font-weight: 800;
    color: var(--silver);
    line-height: 1;
    letter-spacing: -3px;
  }
  .cover--page .billboard-word { left: 526px; top: 77px; font-size: 134px; }
  .cover--channel .billboard-word { left: 533px; top: 26px; font-size: 136px; }

  .firm-name {
    position: absolute;
    display: flex; align-items: center; gap: 7px;
    font-family: "EB Garamond", serif;
    font-weight: 600;
    color: var(--navy);
    text-transform: uppercase;
  }
  .firm-mark { background: var(--navy); flex: none; }
  .firm-name span { display: block; }
  .firm-name .firm-name__lead { font-size: 0.5em; line-height: 1; }
  .cover--page .firm-name { left: 505px; top: 28px; font-size: 15px; line-height: 1.05; }
  .cover--page .firm-mark { width: 34px; height: 34px; }
  .cover--channel .firm-name { left: 745px; top: 51px; font-size: 22px; line-height: 1.05; gap: 9px; }
  .cover--channel .firm-mark { width: 52px; height: 52px; }

  .practice {
    position: absolute;
    font-weight: 600;
    color: var(--ink);
    letter-spacing: 2.4px;
    text-transform: uppercase;
  }
  .cover--page .practice { left: 283px; width: 436px; top: 209px; text-align: center; font-size: 13px; }
  .cover--channel .practice { right: 41px; top: 115px; text-align: right; font-size: 11.5px; line-height: 19.5px; letter-spacing: 2.6px; }

  .web-address {
    position: absolute;
    font-size: 10.5px;
    letter-spacing: 1.6px;
    color: var(--ink);
  }
  .web-address strong { font-weight: 600; }
  .cover--page .web-address {
    left: 283px; width: 436px; top: 237px;
    display: flex; justify-content: center; align-items: center; gap: 18px;
  }
  .cover--page .web-address::before,
  .cover--page .web-address::after {
    content: ""; width: 65px; height: 1px; background: var(--ink); opacity: 0.7;
  }
  .cover--channel .web-address { right: 41px; top: 24px; }
</style>
</head>
<body>

  <p class="format-label format-label--page">FOR FRIENDBOOK</p>

  <section class="cover cover--page">
    <div class="tagline-panel">
      <h1 class="tagline">
        <strong><span>Central</span></strong>
        <span>Pennslyvania's</span>
        <span>Premier Family</span>
        <strong><span>Law Firm</span></strong>
      </h1>
      <div class="tagline-rule"></div>
    </div>
    <div class="firm-name">
      <div class="firm-mark"></div>
      <div><span class="firm-name__lead">The Law Office of</span><span>Miles T. Hadley</span></div>
    </div>
    <div class="rings" role="img" aria-label="Silver wedding band and diamond engagement ring standing upright as the letters Y and I"></div>
    <div class="billboard-word" aria-label="YIKE">KE</div>
    <p class="practice">Family Lawyer (Divorce and Custody)</p>
    <p class="web-address"><span>www.<strong>MilesHadleyLaw</strong>.com</span></p>
  </section>

  <p class="format-label format-label--channel">FOR VIEWTUBE</p>

  <section class="cover cover--channel">
    <div class="tagline-panel">
      <h2 class="tagline">
        <strong><span>Central</span></strong>
        <span>Pennslyvania's</span>
        <span>Premier Family</span>
        <strong><span>Law Firm</span></strong>
      </h2>
    </div>
    <div class="rings" role="img" aria-label="Silver wedding band and diamond engagement ring standing upright as the letters Y and I"></div>
    <div class="billboard-word" aria-label="YIKE">KE</div>
    <p class="web-address">www.<strong>MilesHadleyLaw</strong>.com</p>
    <div class="firm-name">
      <div class="firm-mark"></div>
      <div><span class="firm-name__lead">The Law Office of</span><span>Miles T. Hadley</span></div>
    </div>
    <p class="practice">Family Lawyer<br>(Divorce and Custody)</p>
  </section>

</body>
</html>
```